Gravaloop bottle design

We're a small company looking for someone to help with our bottle design. We provide a sauce that will boost the flavor of packaged ramen. We're looking for a label that will stand out. I'm attaching some of the labels we like and some that I've made.

```html
<!DOCTYPE html>
<html lang="en">
<head>
<meta charset="utf-8">
<title>Gravaloop Ramen Sauce Label</title>
<link href="https://fonts.googleapis.com/css2?family=Poppins:wght@700;800&display=swap" rel="stylesheet">
<style>
  :root {
    --orange: #f06a24;
    --teal-dark: #0f4251;
    --teal-light: #4fb3bf;
    --cream: #f6f5c4;
    --gold: #f4b526;
  }
  html, body {
    margin: 0;
    padding: 0;
    width: 763px;
    height: 1200px;
    overflow: hidden;
    background: var(--orange);
  }
  .canvas {
    position: relative;
    width: 763px;
    height: 1200px;
    background: var(--orange);
  }
  .label {
    position: absolute;
    left: 51px;
    top: 351px;
    width: 660px;
    height: 498px;
    filter: drop-shadow(0 3px 4px rgba(0,0,0,0.18));
  }
  .label text {
    font-family: "Poppins", sans-serif;
    font-weight: 700;
  }
  .brand-name { fill: var(--cream); font-weight: 800; }
  .product-type { fill: var(--cream); }
  .volume { fill: var(--cream); }
  .badge-text { fill: var(--teal-dark); }
</style>
</head>
<body>
<main class="canvas">
  <svg class="label" viewBox="0 0 590 445" xmlns="http://www.w3.org/2000/svg" aria-label="Gravaloop ramen sauce bottle label">
    <!-- label base -->
    <rect class="label-edge" x="0" y="0" width="590" height="445" rx="14" fill="var(--cream)"/>
    <rect class="label-panel" x="7" y="7" width="576" height="431" rx="6" fill="var(--teal-dark)"/>
    <rect class="label-border-band" x="16" y="16" width="558" height="413" fill="none" stroke="var(--teal-light)" stroke-width="5" role="img" aria-label="Zigzag border pattern"/>

    <!-- badge -->
    <g class="badge">
      <ellipse cx="73" cy="57" rx="42" ry="25" fill="var(--orange)"/>
      <ellipse cx="73" cy="57" rx="44" ry="27" fill="none" stroke="var(--orange)" stroke-width="7" stroke-dasharray="3 3"/>
      <text class="badge-text" x="73" y="53" font-size="13" text-anchor="middle">OHIO'S</text>
      <text class="badge-text" x="73" y="69" font-size="13" text-anchor="middle">BEST</text>
    </g>

    <!-- central oval -->
    <ellipse class="oval-rim" cx="295" cy="224" rx="268" ry="172" fill="var(--cream)"/>
    <ellipse class="oval-field" cx="295" cy="224" rx="258" ry="162" fill="var(--orange)"/>

    <!-- illustration area -->
    <circle class="bowl-illustration" cx="295" cy="112" r="44" fill="var(--gold)" opacity="0.85" role="img" aria-label="Illustration of a noodle bowl with chopsticks"/>

    <!-- type -->
    <text class="brand-name" x="295" y="286" font-size="84" text-anchor="middle" textLength="470" lengthAdjust="spacingAndGlyphs">GRAVALOOP</text>
    <text class="product-type" x="295" y="358" font-size="17" text-anchor="middle">RAMEN SAUCE</text>
    <text class="volume" x="544" y="403" font-size="14" text-anchor="end">330 ML</text>
  </svg>
</main>
</body>
</html>
```